Bellwood Advisors
Name of the Person: Miranda Holloway President
Address 427 Linden Grove Road New York N.Y 10135
Tel: 212 555 0193
Cell: 917 555 02 47
Email:tlandrinc@quorvane.com

Please use the logo idea of Pelvarine Change the sense of the arrow do it from right to left
Pantone color for the logo 300 U
For the word strategist use 300U
Please use same fonts or very similar as the one use in Pelvarine
Please use same lay out as Pelvarine if you can

Industry/Entity Type

Consulting

Logo Text

TL&R CONSULTING Inc

```html
<!DOCTYPE html>
<html lang="en">
<head>
<meta charset="utf-8">
<title>TL&amp;R Consulting Inc — Business Card</title>
<link rel="stylesheet" href="https://fonts.googleapis.com/css2?family=Barlow:wght@500&family=Arimo:wght@400;700&display=swap">
<style>
  :root {
    --brand-blue: #1b7cc4;
    --text-grey: #5a5a5a;
    --card-white: #ffffff;
    --page-bg: #ffffff;
    --card-edge: #e6e6e6;
  }
  * { margin: 0; padding: 0; box-sizing: border-box; }
  html, body {
    width: 963px;
    height: 1200px;
    overflow: hidden;
    background: var(--page-bg);
  }
  .sheet {
    position: relative;
    width: 963px;
    height: 1200px;
  }
  .card {
    position: absolute;
    top: 478px;
    width: 440px;
    height: 244px;
    background: var(--card-white);
    border: 1px solid var(--card-edge);
    box-shadow: 4px 5px 8px rgba(0, 0, 0, 0.35);
    overflow: hidden;
  }
  .card--front { left: 31px; }
  .card--back { left: 492px; }

  .brand-band {
    position: absolute;
    left: 0;
    right: 0;
    bottom: 0;
    height: 33px;
    background: var(--brand-blue);
  }
  .brand-mark {
    position: absolute;
    border-radius: 50%;
    background: var(--brand-blue);
  }
  .brand-name {
    position: absolute;
    font-family: "Barlow", sans-serif;
    font-weight: 500;
    color: var(--brand-blue);
    line-height: 1;
    white-space: nowrap;
  }

  /* Front */
  .card--front .brand-mark {
    left: 165px;
    top: 21px;
    width: 110px;
    height: 110px;
  }
  .card--front .brand-name {
    left: 0;
    right: 0;
    top: 151px;
    text-align: center;
    font-size: 50px;
  }
  .card--front .brand-band {
    font-family: "Arimo", sans-serif;
    font-size: 15px;
    color: #ffffff;
    letter-spacing: 0.3px;
    line-height: 33px;
    padding-left: 163px;
  }

  /* Back */
  .card--back .brand-mark {
    left: 22px;
    top: 19px;
    width: 88px;
    height: 88px;
  }
  .card--back .brand-name {
    left: 131px;
    top: 38px;
    font-size: 40px;
  }
  .brand-descriptor {
    position: absolute;
    left: 131px;
    top: 80px;
    font-family: "Arimo", sans-serif;
    font-size: 12.5px;
    color: var(--text-grey);
    letter-spacing: 0.3px;
  }
  .tagline {
    position: absolute;
    right: 19px;
    top: 56px;
    font-family: "Arimo", sans-serif;
    font-size: 13px;
    line-height: 1.05;
    text-align: right;
  }
  .tagline__top {
    display: block;
    color: var(--text-grey);
    letter-spacing: 1.6px;
    text-transform: uppercase;
  }
  .tagline__bottom {
    display: block;
    color: var(--brand-blue);
    letter-spacing: 0.8px;
    text-transform: lowercase;
  }
  .holder {
    position: absolute;
    left: 24px;
    top: 138px;
    width: 152px;
    text-align: right;
    font-family: "Arimo", sans-serif;
    line-height: 1.2;
  }
  .holder__name {
    display: block;
    font-size: 13px;
    font-weight: 400;
    color: var(--text-grey);
    text-transform: uppercase;
    letter-spacing: 0.2px;
    white-space: nowrap;
  }
  .holder__role {
    display: block;
    font-size: 14px;
    color: var(--brand-blue);
  }
  .contact {
    position: absolute;
    left: 193px;
    top: 139px;
    list-style: none;
    font-family: "Arimo", sans-serif;
    font-size: 11.3px;
    line-height: 16.3px;
    color: var(--text-grey);
    white-space: nowrap;
  }
</style>
</head>
<body>
<main class="sheet">

  <section class="card card--front" aria-label="Card front">
    <span class="brand-mark" aria-hidden="true"></span>
    <div class="brand-name">TL&amp;R</div>
    <div class="brand-band">CONSULTING Inc</div>
  </section>

  <section class="card card--back" aria-label="Card back">
    <span class="brand-mark" aria-hidden="true"></span>
    <div class="brand-name">TL&amp;R</div>
    <div class="brand-descriptor">CONSULTING Inc</div>

    <p class="tagline">
      <span class="tagline__top">Bellwood</span>
      <span class="tagline__bottom">Advisors</span>
    </p>

    <p class="holder">
      <span class="holder__name">Miranda Holloway</span>
      <span class="holder__role">President</span>
    </p>

    <ul class="contact">
      <li>427 Linden Grove Road New York N.Y 10135</li>
      <li>Tel. 212 555 0193</li>
      <li>Cell. 917 555 02 47</li>
      <li>Email. tlandrinc@quorvane.com</li>
    </ul>

    <div class="brand-band"></div>
  </section>

</main>
</body>
</html>
```